Website Design for Kindred Harbor Network

Please design and code a new website.
Here are the sites I like best:
http://www.voyaglint.com/alternate/
http://www.wheelsbrevant.org
Please make it similar but look at the competitor site (below) for images and wording. This is NOT a car donation site. It's a senior lead placement site like https://www.elderbrookhaven.com. I just like this sites above as a lead generation sites.
Competitor site:
https://www.elderbrookhaven.com (use ideas / verbiage from this site)
Updates
Competitor site:

```html
<!DOCTYPE html>
<html lang="en">
<head>
<meta charset="utf-8">
<title>Kindred Harbor Network — Senior Living Advice</title>
<link rel="stylesheet" href="https://fonts.googleapis.com/css2?family=Montserrat:wght@500;600;700;800&family=Roboto:wght@400;500;700&display=swap">
<style>
:root{
  --navy:#0f2c86;
  --navy-deep:#0a1d5e;
  --red:#c8141e;
  --red-deep:#a60f17;
  --gold:#f5ae3d;
  --ink:#2a2f45;
  --muted:#5b6072;
  --grey:#e3e3e6;
  --line:#cfd2dc;
  --canvas:#eceefa;
  --white:#ffffff;
}
*{box-sizing:border-box;margin:0;padding:0}
html,body{width:1200px;height:3820px;overflow:hidden}
body{background:var(--canvas);font-family:"Roboto",Arial,sans-serif;color:var(--ink)}
.page{position:absolute;left:165px;top:0;width:870px;height:3820px;background:var(--white);overflow:hidden}
.heading{font-family:"Montserrat",Arial,sans-serif;font-weight:800;color:var(--navy);text-transform:uppercase;text-align:center;letter-spacing:.5px}
.heading .accent{color:var(--red)}
.btn{display:inline-block;font-family:"Montserrat",Arial,sans-serif;font-weight:700;font-size:12px;text-transform:uppercase;color:var(--white);background:var(--navy);padding:9px 22px;border-radius:3px;letter-spacing:.5px}

/* Header */
.topbar{height:95px;background:linear-gradient(100deg,var(--navy-deep) 0%,#1b3a92 55%,#142f7c 100%);position:relative}
.logo{position:absolute;left:28px;top:30px;font-family:"Montserrat",Arial,sans-serif;font-weight:700;font-size:26px;color:var(--white)}
.top-tools{position:absolute;right:26px;top:38px;display:flex;gap:6px;align-items:center}
.top-tools span{width:16px;height:16px;border:1px solid rgba(255,255,255,.7);border-radius:2px}
.top-tools .lang{width:auto;border:none;color:var(--white);font-size:11px;margin-left:6px}
.nav{height:32px;background:var(--navy-deep);display:flex;justify-content:space-between;align-items:center;padding:0 18px;border-top:1px solid rgba(255,255,255,.15)}
.nav a{font-family:"Montserrat",Arial,sans-serif;font-weight:700;font-size:11px;color:var(--white);text-decoration:none;text-transform:uppercase}

/* Hero */
.hero{position:relative;height:398px}
.hero-photo{position:absolute;inset:0;background:linear-gradient(120deg,#9fb46a 0%,#6f8c48 35%,#c9c7b0 60%,#7e9a55 100%)}
.lead-form{position:absolute;left:548px;top:16px;width:258px;height:366px;background:var(--red);padding:14px 16px}
.lead-call{display:flex;gap:10px;align-items:center;color:var(--white);padding-bottom:12px;border-bottom:1px solid rgba(255,255,255,.4);margin-bottom:12px}
.lead-call .ring{width:42px;height:42px;border-radius:50%;border:2px solid var(--white);display:flex;align-items:center;justify-content:center;flex:none}
.lead-call b{display:block;font-family:"Montserrat",Arial,sans-serif;font-size:13px}
.lead-call strong{display:block;font-family:"Montserrat",Arial,sans-serif;font-size:21px;font-weight:800}
.lead-call small{font-size:10px}
.field{height:22px;background:var(--white);margin-bottom:8px;font-size:10px;color:var(--muted);padding:5px 7px}
.field.tall{height:92px}
.lead-form .btn{margin-top:4px;padding:7px 16px;font-size:11px}

/* Why choose us */
.why{position:relative;height:181px;background:var(--grey);display:flex}
.why-title{width:185px;background:linear-gradient(160deg,#1e3e9a,var(--navy-deep));clip-path:polygon(0 0,100% 0,100% 100%,0 100%);padding:50px 0 0 22px;font-family:"Montserrat",Arial,sans-serif;font-weight:800;font-size:26px;line-height:1.05;color:var(--gold);text-transform:uppercase}
.why-list{flex:1;display:flex;justify-content:space-around;padding:34px 16px 0}
.why-item{width:100px;text-align:center;font-size:11px;color:var(--navy);line-height:1.3}
.why-item svg{display:block;margin:0 auto 10px}

/* How it works */
.how{height:472px;padding-top:50px}
.rule-head{display:flex;align-items:center;justify-content:center;gap:26px;font-size:21px}
.rule-head::before,.rule-head::after{content:"";width:150px;height:1px;background:var(--line)}
.steps{display:flex;justify-content:space-between;padding:60px 42px 0}
.step{width:170px;text-align:center}
.step svg{display:block;margin:0 auto 22px}
.step h3{font-family:"Montserrat",Arial,sans-serif;font-size:13px;color:var(--navy);font-weight:700;line-height:1.35;min-height:36px;margin-bottom:12px}
.step p{font-size:11px;line-height:1.5;color:var(--muted);text-align:left}

/* Spokesperson */
.spokes{position:relative;height:344px}
.spokes-photo{position:absolute;inset:0;background:linear-gradient(90deg,#c9b59a 0%,#d8c6a9 40%,#b9a48a 70%,#9c8a74 100%)}
.spokes-card{position:absolute;left:28px;top:108px;width:364px;height:206px;background:var(--white);border-radius:10px;padding:46px 24px 0;box-shadow:0 4px 14px rgba(0,0,0,.15)}
.avatar{position:absolute;left:174px;top:-38px;width:76px;height:76px;border-radius:50%;background:linear-gradient(#8a7b70,#c7b8a8);border:4px solid var(--white)}
.spokes-card h4{font-family:"Montserrat",Arial,sans-serif;font-size:13px;color:var(--navy);margin-bottom:14px}
.spokes-card p{font-size:10px;line-height:1.55;color:var(--muted);text-align:center}
.spokes-call{position:absolute;left:480px;top:150px;text-align:center;width:360px}
.spokes-call p{font-family:"Montserrat",Arial,sans-serif;font-weight:700;font-size:22px;color:var(--navy)}
.spokes-call strong{font-family:"Montserrat",Arial,sans-serif;font-weight:800;font-size:28px;color:var(--red)}

/* FAQ */
.faq{height:531px;padding-top:62px;position:relative}
.faq .heading{font-size:21px}
.aid{position:absolute;left:0;top:133px;width:420px;height:325px;display:flex}
.aid-text{width:210px;background:var(--gold);padding:90px 14px 0 22px;font-family:"Montserrat",Arial,sans-serif;font-weight:800;color:var(--navy);text-align:center}
.aid-text .small{font-size:20px}
.aid-text .big{font-size:44px;color:var(--red);line-height:1.05}
.aid-text .mid{font-size:19px;line-height:1.2}
.aid-text .btn{margin-top:26px}
.aid-photo{flex:1;background:linear-gradient(180deg,#9a958a,#6d6a64 60%,#b9b3a6)}
.accordion{position:absolute;left:455px;top:133px;width:413px}
.qa{border:1px solid var(--line);border-radius:14px;margin-bottom:9px;padding:9px 16px;font-size:11px;font-weight:700;display:flex;justify-content:space-between;align-items:center}
.qa.open{display:block;border-radius:14px;padding-bottom:12px}
.qa.open .q{display:flex;justify-content:space-between;margin-bottom:8px}
.qa.open p{font-weight:400;color:var(--muted);line-height:1.5;font-size:10.5px}

/* Advisor finder */
.finder{position:relative;height:319px;text-align:center}
.finder-photo{position:absolute;inset:0;background:linear-gradient(180deg,rgba(20,45,140,.85),rgba(15,40,130,.92)),linear-gradient(90deg,#3f5a8a,#5c6f8f)}
.finder-inner{position:relative;padding-top:92px;color:var(--white)}
.finder .heading{color:var(--white);font-size:22px}
.finder p{font-size:12px;margin:6px 0 18px}
.finder .field{width:250px;margin:0 auto 8px;text-align:left}
.finder .btn{background:var(--red);width:250px;padding:7px}

/* States */
.states{height:604px;padding-top:78px}
.states .heading{font-size:20px}
.tabs{display:flex;justify-content:center;gap:40px;margin:56px 0 0;font-family:"Montserrat",Arial,sans-serif;font-size:12px;font-weight:600;color:var(--muted);border-bottom:1px solid var(--line);padding-bottom:10px;margin-left:40px;margin-right:40px}
.tabs .active{color:var(--navy);font-weight:700;position:relative}
.tabs .active::after{content:"";position:absolute;left:0;right:0;bottom:-11px;height:3px;background:var(--navy)}
.state-cols{display:flex;padding:30px 0 0 28px;gap:0}
.state-cols ul{list-style:none;width:214px}
.state-cols li{font-size:12px;font-weight:700;color:var(--navy);line-height:17px}

/* Reviews */
.reviews{height:478px;background:var(--grey);text-align:center;padding-top:32px}
.reviews .heading{font-size:20px;line-height:1.3}
.faces{display:flex;justify-content:center;gap:10px;margin:38px 0 64px}
.faces span{width:80px;height:80px;border-radius:50%;border:3px solid var(--white);background:linear-gradient(#c9c2bb,#a8a099)}
.reviews blockquote{width:640px;margin:0 auto;font-size:12px;line-height:1.55;color:var(--ink)}
.reviews cite{display:block;margin:10px 0 22px;font-style:normal;font-size:12px;color:var(--muted)}

/* Footer */
.footer{position:relative;height:334px;background:linear-gradient(160deg,#1c3c9c,var(--navy-deep))}
.footer-logo{position:absolute;left:0;right:0;top:38px;text-align:center;font-family:"Montserrat",Arial,sans-serif;font-weight:700;font-size:26px;color:var(--white)}
.footer-cols{position:absolute;left:26px;right:16px;top:112px;display:flex;gap:40px;color:var(--white)}
.footer-cols h5{font-family:"Montserrat",Arial,sans-serif;font-size:12px;margin-bottom:10px;padding-bottom:6px;border-bottom:1px solid rgba(255,255,255,.35);text-transform:uppercase}
.about{width:250px;font-size:11px;line-height:1.55}
.links{width:200px}
.links li{list-style:none;font-size:10px;font-weight:700;text-transform:uppercase;line-height:17px}
.footer-call{margin-top:52px;width:270px;height:74px;border:2px solid var(--white);border-radius:10px;display:flex;gap:12px;align-items:center;padding:0 14px}
.footer-call b{display:block;font-family:"Montserrat",Arial,sans-serif;font-size:13px}
.footer-call strong{display:block;font-family:"Montserrat",Arial,sans-serif;font-size:20px;font-weight:800}
.footer-call small{font-size:10px}
.copyright{height:32px;background:var(--white);font-size:10px;color:var(--muted);text-align:center;line-height:32px}
</style>
</head>
<body>
<div class="page">

  <header>
    <div class="topbar">
      <div class="logo">Kindred Harbor Network</div>
      <div class="top-tools"><span></span><span></span><span></span><span></span><span class="lang">Eng ▾</span></div>
    </div>
    <nav class="nav">
      <a>Assisted Living</a><a>Memory Care</a><a>Nursing Homes</a><a>More Living Options</a><a>Planning &amp; Advice</a><a>How Our Service Works</a>
    </nav>
  </header>

  <section class="hero">
    <div class="hero-photo" role="img" aria-label="Photo of a senior man embracing a younger family member outdoors in a park"></div>
    <form class="lead-form">
      <div class="lead-call">
        <div class="ring"><svg width="20" height="20" viewBox="0 0 24 24"><path d="M6.6 10.8a15 15 0 0 0 6.6 6.6l2.2-2.2c.3-.3.7-.4 1-.2 1.1.4 2.3.6 3.6.6.6 0 1 .4 1 1V20c0 .6-.4 1-1 1A17 17 0 0 1 3 4c0-.6.4-1 1-1h3.5c.6 0 1 .4 1 1 0 1.3.2 2.5.6 3.6.1.3 0 .7-.2 1z" fill="#fff"/></svg></div>
        <div><b>NEED HELP? CALL NOW</b><strong>0-000-000-0000</strong><small>Find Senior Living Near You</small></div>
      </div>
      <div class="field">First Name</div>
      <div class="field">Last Name</div>
      <div class="field">Email</div>
      <div class="field">Zip Code</div>
      <div class="field tall">Message</div>
      <span class="btn">Submit</span>
    </form>
  </section>

  <section class="why">
    <div class="why-title">Why<br>Choose Us</div>
    <div class="why-list">
      <div class="why-item"><svg width="34" height="34" viewBox="0 0 34 34"><circle cx="17" cy="10" r="6" fill="#0f2c86"/><path d="M5 32c0-8 5-12 12-12s12 4 12 12z" fill="#0f2c86"/></svg>Distinctive local advisor</div>
      <div class="why-item"><svg width="34" height="34" viewBox="0 0 34 34"><rect x="5" y="4" width="24" height="28" rx="2" fill="none" stroke="#0f2c86" stroke-width="3"/><path d="M10 13h14M10 19h14M10 25h9" stroke="#0f2c86" stroke-width="3"/></svg>Have picked list of communities to match your needs</div>
      <div class="why-item"><svg width="34" height="34" viewBox="0 0 34 34"><circle cx="17" cy="17" r="14" fill="none" stroke="#0f2c86" stroke-width="3"/><text x="17" y="23" text-anchor="middle" font-size="17" font-weight="700" fill="#0f2c86" font-family="Arial,sans-serif">$</text></svg>Full details and pricing</div>
      <div class="why-item"><svg width="34" height="34" viewBox="0 0 34 34"><rect x="4" y="7" width="26" height="24" rx="2" fill="#0f2c86"/><path d="M4 14h26" stroke="#fff" stroke-width="2"/><rect x="10" y="3" width="3" height="7" fill="#0f2c86"/><rect x="21" y="3" width="3" height="7" fill="#0f2c86"/></svg>Help scheduling tours</div>
      <div class="why-item"><svg width="40" height="34" viewBox="0 0 40 34"><path d="M3 24V15l5-7h18l5 7h5v9z" fill="#0f2c86"/><circle cx="11" cy="26" r="4" fill="#0f2c86" stroke="#e3e3e6" stroke-width="2"/><circle cx="29" cy="26" r="4" fill="#0f2c86" stroke="#e3e3e6" stroke-width="2"/></svg>Move-in support</div>
    </div>
  </section>

  <section class="how">
    <h2 class="heading rule-head"><span>How Our Service <span class="accent">Works</span></span></h2>
    <div class="steps">
      <div class="step">
        <svg width="50" height="46" viewBox="0 0 50 46"><circle cx="13" cy="10" r="6" fill="#c8141e"/><circle cx="37" cy="10" r="6" fill="#c8141e"/><path d="M3 40V26c0-5 4-8 10-8s10 3 10 8v14zM27 40V26c0-5 4-8 10-8s10 3 10 8v14z" fill="#c8141e"/><rect x="18" y="30" width="14" height="3" fill="#c8141e"/></svg>
        <h3>Talk with your local advisor</h3>
        <p>Contrary to popular belief, Lorem Ipsum is not simply random text. It has roots in a piece of classical Latin literature.</p>
      </div>
      <div class="step">
        <svg width="50" height="46" viewBox="0 0 50 46"><circle cx="16" cy="8" r="6" fill="#c8141e"/><circle cx="34" cy="8" r="6" fill="#c8141e"/><path d="M9 44V18h14v26zM27 44V18h14v26z" fill="#c8141e"/><path d="M44 22v22" stroke="#c8141e" stroke-width="3"/></svg>
        <h3>Get information on care options</h3>
        <p>Contrary to popular belief, Lorem Ipsum is not simply random text. It has roots in a piece of classical Latin literature.</p>
      </div>
      <div class="step">
        <svg width="50" height="46" viewBox="0 0 50 46"><circle cx="25" cy="8" r="6" fill="#c8141e"/><circle cx="10" cy="16" r="5" fill="#c8141e"/><circle cx="40" cy="16" r="5" fill="#c8141e"/><path d="M17 44V22h16v22zM3 44V28h12v16zM35 44V28h12v16z" fill="#c8141e"/></svg>
        <h3>Choose communities to visit</h3>
        <p>Contrary to popular belief, Lorem Ipsum is not simply random text. It has roots in a piece of classical Latin literature.</p>
      </div>
      <div class="step">
        <svg width="50" height="46" viewBox="0 0 50 46"><rect x="14" y="6" width="24" height="38" fill="#c8141e"/><path d="M19 12h4M29 12h4M19 20h4M29 20h4M19 28h4M29 28h4" stroke="#fff" stroke-width="3"/><circle cx="9" cy="12" r="7" fill="#c8141e" stroke="#fff" stroke-width="2"/><circle cx="9" cy="12" r="2.5" fill="#fff"/></svg>
        <h3>Transition to new home</h3>
        <p>Contrary to popular belief, Lorem Ipsum is not simply random text. It has roots in a piece of classical Latin literature.</p>
      </div>
    </div>
  </section>

  <section class="spokes">
    <div class="spokes-photo" role="img" aria-label="Photo of seniors chatting together in a bright community lounge"></div>
    <div class="spokes-card">
      <div class="avatar" role="img" aria-label="Portrait of the network spokesperson"></div>
      <h4>Marion T. - Kindred Harbor Network spokesperson</h4>
      <p>There are many variations of passages of Lorem Ipsum available, but the majority have suffered alteration in some form, by injected humour, or randomised words which don't look even slightly believable. If you are going to use a passage of Lorem Ipsum, you need to be sure there isn't anything embarrassing hidden in the middle of text.</p>
    </div>
    <div class="spokes-call">
      <p>There's no cost to you</p>
      <strong>Call: 0-000-000-0000</strong>
    </div>
  </section>

  <section class="faq">
    <h2 class="heading">Frequently Asked <span class="accent">Questions</span></h2>
    <div class="aid">
      <div class="aid-text">
        <div class="small">Access up to</div>
        <div class="big">$2,000</div>
        <div class="mid">per month in veteran's aid</div>
        <span class="btn">Learn More</span>
      </div>
      <div class="aid-photo" role="img" aria-label="Photo of a senior veteran in a suit wearing service medals"></div>
    </div>
    <div class="accordion">
      <div class="qa open"><div class="q"><span>Lorem Ipsum is simply dummy text</span><span>⌄</span></div><p>Contrary to popular belief, Lorem Ipsum is not simply random text. It has roots in a piece of classical Latin literature from 45 BC, making it over 2000 years old.</p></div>
      <div class="qa"><span>Lorem Ipsum is simply dummy text</span><span>⌄</span></div>
      <div class="qa"><span>Lorem Ipsum is simply dummy text</span><span>⌄</span></div>
      <div class="qa"><span>Lorem Ipsum is simply dummy text</span><span>⌄</span></div>
      <div class="qa"><span>Lorem Ipsum is simply dummy text</span><span>⌄</span></div>
      <div class="qa"><span>Lorem Ipsum is simply dummy text</span><span>⌄</span></div>
      <div class="qa"><span>Lorem Ipsum is simply dummy text</span><span>⌄</span></div>
    </div>
  </section>

  <section class="finder">
    <div class="finder-photo" role="img" aria-label="Photo of a quiet tree-lined residential street under a blue overlay"></div>
    <div class="finder-inner">
      <h2 class="heading">Find Your <span class="accent">Local Advisor</span></h2>
      <p>Lorem Ipsum is simply dummy text of the printing and typesetting industry</p>
      <div class="field">Enter your city, or postal code</div>
      <span class="btn">Find Advisor</span>
    </div>
  </section>

  <section class="states">
    <h2 class="heading">Senior Living <span class="accent">by State</span></h2>
    <div class="tabs"><span>Assisted Living</span><span class="active">Memory Care</span><span>Independent Living</span><span>Nursing Home</span><span>Care Homes</span></div>
    <div class="state-cols">
      <ul><li>Alabama</li><li>Alaska</li><li>Arizona</li><li>Arkansas</li><li>California</li><li>Colorado</li><li>Connecticut</li><li>Delaware</li><li>District of Columbia</li><li>Florida</li><li>Georgia</li><li>Hawaii</li><li>Idaho</li><li>Illinois</li><li>Indiana</li></ul>
      <ul><li>Iowa</li><li>Kansas</li><li>Kentucky</li><li>Louisiana</li><li>Maine</li><li>Maryland</li><li>Massachusetts</li><li>Michigan</li><li>Minnesota</li><li>Mississippi</li><li>Missouri</li><li>Montana</li><li>Nebraska</li><li>Nevada</li></ul>
      <ul><li>New Hampshire</li><li>New Jersey</li><li>New Mexico</li><li>New York</li><li>North Carolina</li><li>North Dakota</li><li>Ohio</li><li>Oklahoma</li><li>Oregon</li><li>Pennsylvania</li><li>Rhode Island</li><li>South Carolina</li><li>South Dakota</li><li>Tennessee</li></ul>
      <ul><li>Texas</li><li>Utah</li><li>Vermont</li><li>Virginia</li><li>Washington</li><li>West Virginia</li><li>Wisconsin</li><li>Wyoming</li></ul>
    </div>
  </section>

  <section class="reviews">
    <h2 class="heading">82% of Our Customers<br><span class="accent">Recommend Our Service</span></h2>
    <div class="faces">
      <span role="img" aria-label="Customer portrait"></span>
      <span role="img" aria-label="Customer portrait"></span>
      <span role="img" aria-label="Customer portrait"></span>
      <span role="img" aria-label="Customer portrait"></span>
    </div>
    <blockquote>There are many variations of passages of Lorem Ipsum available, but the majority have suffered alteration in some form, by injected humour, or randomised words which don't look even slightly believable</blockquote>
    <cite>Walter B., OR</cite>
    <span class="btn">View More</span>
  </section>

  <footer>
    <div class="footer">
      <div class="footer-logo">Kindred Harbor Network</div>
      <div class="footer-cols">
        <div class="about"><h5>About Us</h5><p>Lorem Ipsum is simply dummy text of the printing and typesetting industry. Lorem Ipsum has been the industry's standard dummy text ever since the 1500s, when an unknown printer took a galley of type and scrambled it to make a type specimen book.</p></div>
        <div class="links"><h5>Links</h5><ul><li>Assisted Living</li><li>Memory Care</li><li>Nursing Homes</li><li>More Living Options</li><li>Planning &amp; Advice</li><li>How Our Service Works</li></ul></div>
        <div class="footer-call">
          <svg width="40" height="40" viewBox="0 0 40 40"><circle cx="20" cy="20" r="18" fill="none" stroke="#fff" stroke-width="2"/><path d="M14 17a13 13 0 0 0 9 9l2.2-2.2c.3-.3.7-.4 1-.2 1 .4 2 .5 3 .5.5 0 .8.4.8.8V28c0 .5-.3.8-.8.8A17 17 0 0 1 11 11.8c0-.5.3-.8.8-.8h3c.5 0 .8.3.8.8 0 1 .2 2 .5 3 .1.3 0 .7-.2 1z" fill="#fff"/></svg>
          <div><b>NEED HELP? CALL NOW</b><strong>0-000-000-0000</strong><small>Find Senior Living Near You</small></div>
        </div>
      </div>
    </div>
    <div class="copyright">© Copyright Kindred Harbor Network 2019</div>
  </footer>

</div>
</body>
</html>
```